Graphic to show our studio's values

We'd like to create a graphic of our values that can go onto fun gifts for our team in order to keep our values in front of all of us in a creative way. The graphic might go onto mugs, gift boxes, tote bags, etc. We are a growing interior architecture/design studio in Austin, TX. I encourage you to check out our website at www.morvankestudio.com to get a sense of our vibe and culture. The graphic may or may not include the subtext to each value depending on how difficult it is to incorporate the subtext into a great design.

```html
<!DOCTYPE html>
<html lang="en">
<head>
<meta charset="utf-8">
<title>Our Values – We Are</title>
<link rel="stylesheet" href="https://fonts.googleapis.com/css2?family=Josefin+Sans:wght@600;700&display=swap">
<style>
  :root {
    --backdrop: #cccccc;
    --slate: #626366;
    --lime: #b4cd45;
    --white: #ffffff;
  }
  html, body {
    margin: 0;
    padding: 0;
    width: 1100px;
    height: 1200px;
    overflow: hidden;
    background: var(--backdrop);
  }
  .values-board {
    display: block;
    width: 1100px;
    height: 1200px;
    font-family: "Josefin Sans", "Futura", sans-serif;
    font-weight: 700;
  }
  .panel--light { --panel-bg: var(--white); --box-bg: var(--slate); --box-ink: var(--white); --accent: var(--slate); --tag-ink: var(--white); }
  .panel--dark  { --panel-bg: var(--slate); --box-bg: var(--white); --box-ink: var(--slate); --accent: var(--white); --tag-ink: var(--slate); }

  .panel-bg   { fill: var(--panel-bg); }
  .title-box  { fill: var(--box-bg); }
  .title-text { fill: var(--box-ink); font-size: 58px; }
  .tag-band   { fill: var(--lime); }
  .tag-text   { fill: var(--tag-ink); font-size: 42px; }
  .divider    { stroke: var(--accent); stroke-width: 1.6; }
  .value-word { fill: var(--lime); font-size: 44px; }
  .dot        { fill: var(--accent); }
</style>
</head>
<body>
<svg class="values-board" viewBox="0 0 1100 1200" xmlns="http://www.w3.org/2000/svg" role="img" aria-label="Our values. We are learners, positive, trustworthy, responsive.">
  <defs>
    <clipPath id="tag-clip">
      <rect x="111" y="225" width="192" height="53"/>
    </clipPath>
  </defs>

  <g class="panel panel--light" transform="translate(195 218)">
    <rect class="panel-bg" width="711" height="355"/>
    <rect class="title-box" x="35" y="59" width="268" height="142"/>
    <text class="title-text" x="54" y="125" textLength="126" lengthAdjust="spacing">OUR</text>
    <text class="title-text" x="53" y="181" textLength="236" lengthAdjust="spacing">VALUES.</text>
    <rect class="tag-band" x="111" y="225" width="192" height="53"/>
    <g clip-path="url(#tag-clip)">
      <text class="tag-text" x="138" y="266" textLength="140" lengthAdjust="spacing">WE AR</text>
      <text class="tag-text" x="289" y="266">E</text>
    </g>
    <line class="divider" x1="320" y1="59" x2="320" y2="295"/>
    <text class="value-word" x="342" y="97" textLength="237" lengthAdjust="spacing">LEARNERS<tspan class="dot">.</tspan></text>
    <text class="value-word" x="342" y="160" textLength="205" lengthAdjust="spacing">POSITIVE<tspan class="dot">.</tspan></text>
    <text class="value-word" x="340" y="223" textLength="337" lengthAdjust="spacing">TRUSTWORTHY<tspan class="dot">.</tspan></text>
    <text class="value-word" x="342" y="287" textLength="283" lengthAdjust="spacing">RESPONSIVE<tspan class="dot">.</tspan></text>
  </g>

  <g class="panel panel--dark" transform="translate(195 627)">
    <rect class="panel-bg" width="711" height="355"/>
    <rect class="title-box" x="35" y="59" width="268" height="142"/>
    <text class="title-text" x="54" y="125" textLength="126" lengthAdjust="spacing">OUR</text>
    <text class="title-text" x="53" y="181" textLength="236" lengthAdjust="spacing">VALUES.</text>
    <rect class="tag-band" x="111" y="225" width="192" height="53"/>
    <g clip-path="url(#tag-clip)">
      <text class="tag-text" x="138" y="266" textLength="140" lengthAdjust="spacing">WE AR</text>
      <text class="tag-text" x="289" y="266">E</text>
    </g>
    <line class="divider" x1="320" y1="59" x2="320" y2="295"/>
    <text class="value-word" x="342" y="97" textLength="237" lengthAdjust="spacing">LEARNERS<tspan class="dot">.</tspan></text>
    <text class="value-word" x="342" y="160" textLength="205" lengthAdjust="spacing">POSITIVE<tspan class="dot">.</tspan></text>
    <text class="value-word" x="340" y="223" textLength="337" lengthAdjust="spacing">TRUSTWORTHY<tspan class="dot">.</tspan></text>
    <text class="value-word" x="342" y="287" textLength="283" lengthAdjust="spacing">RESPONSIVE<tspan class="dot">.</tspan></text>
  </g>
</svg>
</body>
</html>
```